Business Card Design Project

Need a business card with logo that is attached.
Company name: Moberly Swift Solutions, LLC
My name: Lucia Pembrook
Title: President
Phone number: 703-482-1947
Email: lpembrook@moberlyswiftsolutions.example
web site: www.moberlyswiftsolutions.example

Industry/Entity Type

Business

```html
<!DOCTYPE html>
<html lang="en">
<head>
<meta charset="utf-8">
<title>Moberly Swift Solutions – Business Card</title>
<link rel="stylesheet" href="https://fonts.googleapis.com/css2?family=Cinzel:wght@400&family=Crimson+Text:wght@400&display=swap">
<style>
  :root {
    --bg: #cfd0d2;
    --card: #161718;
    --card-edge: #202224;
    --brand-blue: #1f86c9;
    --brand-teal: #2a9d8f;
    --band-blue: #1689d0;
    --text-light: #e6e6e6;
    --text-muted: #c9c9c9;
    --rule: #f2f2f2;
  }
  * { margin: 0; padding: 0; box-sizing: border-box; }
  html, body { width: 1200px; height: 926px; overflow: hidden; }
  body {
    background: var(--bg);
    display: flex;
    flex-direction: column;
    align-items: center;
    justify-content: center;
    gap: 70px;
  }
  .card {
    position: relative;
    width: 660px;
    height: 378px;
    background: linear-gradient(135deg, var(--card-edge), var(--card) 60%);
    box-shadow: 0 10px 26px rgba(0,0,0,0.28);
    overflow: hidden;
  }
  .brand {
    position: absolute;
    display: flex;
    align-items: center;
    gap: 14px;
  }
  .brand-dot {
    width: 56px;
    height: 56px;
    border-radius: 50%;
    background: var(--brand-teal);
    flex: none;
  }
  .brand-divider {
    width: 2px;
    align-self: stretch;
    background: var(--brand-teal);
  }
  .brand-name {
    font-family: "Crimson Text", serif;
    font-weight: 400;
    font-size: 20px;
    line-height: 1.05;
    letter-spacing: 1.5px;
    text-transform: uppercase;
    color: var(--brand-blue);
  }
  .card-back .brand { left: 50%; top: 50%; transform: translate(-50%, -50%); }
  .card-front .brand { left: 205px; top: 40px; }

  .front-rule {
    position: absolute;
    left: 262px;
    top: 130px;
    width: 2px;
    height: 150px;
    background: var(--rule);
  }
  .front-rule.lower { top: 296px; height: 34px; }
  .holder {
    position: absolute;
    right: 412px;
    top: 158px;
    text-align: right;
    font-family: "Crimson Text", serif;
    color: var(--text-light);
  }
  .holder-name {
    font-size: 21px;
    letter-spacing: 0.5px;
    text-transform: uppercase;
  }
  .holder-title {
    font-size: 13px;
    letter-spacing: 1.5px;
    text-transform: uppercase;
    color: var(--text-muted);
  }
  .contact {
    position: absolute;
    left: 280px;
    top: 190px;
    list-style: none;
    font-family: "Crimson Text", serif;
    font-size: 15.5px;
    line-height: 1.25;
    color: var(--text-muted);
  }
  .band {
    position: absolute;
    left: 0; right: 0; bottom: 0;
    height: 38px;
    background: var(--band-blue);
  }
</style>
</head>
<body>

  <section class="card card-back" aria-label="Business card, back">
    <div class="brand">
      <span class="brand-dot"></span>
      <span class="brand-divider"></span>
      <span class="brand-name">Moberly Swift<br>Solutions<br>LLC</span>
    </div>
  </section>

  <section class="card card-front" aria-label="Business card, front">
    <div class="brand">
      <span class="brand-dot"></span>
      <span class="brand-divider"></span>
      <span class="brand-name">Moberly Swift<br>Solutions<br>LLC</span>
    </div>

    <div class="holder">
      <p class="holder-name">Lucia Pembrook</p>
      <p class="holder-title">President</p>
    </div>

    <span class="front-rule"></span>
    <span class="front-rule lower"></span>

    <ul class="contact">
      <li>Phone: 703-482-1947</li>
      <li>Email: lpembrook@moberlyswiftsolutions.example</li>
      <li>Web site: www.moberlyswiftsolutions.example</li>
    </ul>

    <div class="band"></div>
  </section>

</body>
</html>
```